Website - User Access Door - Images

4 separate images that fit together to form a door that I will animate to open up when a user accesses my website. 1. Left Door 2. Right Door. 3. Lock (open) 4. Lock (closed). High resolution as it must look good on huge monitors.

Attached is a picture very close to what I'm after. I guess the main thing to keep in mind is that it needs to look strong. The attached graphic is quite close to what I'm after, but I need a unique design, not a copy of this one.

Reason: I was promised more than 3 submissions by PixelNook. I guess they need more time...

Here are some images for inspiration. Think Soviet iron nuclear bunker door. Heavy, Strong (but latest technology incorporated)

http://img4.lorvipedia.net/__cb20090716105544/vortra/images/1/1d/KTRF_bunker_door.jpg

http://www.tobiasrenderworks.com/QRT_Bunker3_TobiasKrell.jpg

Nice texture ideas:
http://www.surfacevault.com/data/media/8/steel_door_texture.jpg

Think games:
http://www.stagerundown.com/ironveil/zone7b/24.jpg

http://brightmosaic.com/wp-content/uploads/2013/09/Metal-Door-Wall-Graphic-Decals.jpg

```html
<!DOCTYPE html>
<html lang="en">
<head>
<meta charset="utf-8">
<title>User Access Door – Lock Closed</title>
<link rel="preconnect" href="https://fonts.googleapis.com">
<link href="https://fonts.googleapis.com/css2?family=Roboto:wght@400&display=swap" rel="stylesheet">
<style>
  :root {
    --steel-top: #3b3b3b;
    --steel-mid: #272727;
    --steel-bottom: #0f0f0f;
    --seam-light: #8c8c8c;
    --seam-dark: #050505;
    --ring-light: #8e8e8e;
    --ring-mid: #3c3c3c;
    --ring-dark: #101010;
    --face: #343434;
    --face-dark: #222222;
    --screen: #1a1a1a;
    --screen-frame: #4a4a4a;
    --led: #16c94e;
    --led-glow: #7dffa0;
  }
  html, body {
    margin: 0;
    padding: 0;
    width: 1200px;
    height: 646px;
    overflow: hidden;
    background: var(--steel-bottom);
    font-family: "Roboto", sans-serif;
  }
  .door {
    position: relative;
    width: 1200px;
    height: 646px;
  }
  .door-art {
    display: block;
    width: 1200px;
    height: 646px;
  }
</style>
</head>
<body>
<main class="door">
  <svg class="door-art" viewBox="0 0 1200 646" xmlns="http://www.w3.org/2000/svg">
    <defs>
      <linearGradient id="steel-plate" x1="0" y1="0" x2="0" y2="1">
        <stop offset="0" stop-color="var(--steel-top)"/>
        <stop offset="0.5" stop-color="var(--steel-mid)"/>
        <stop offset="1" stop-color="var(--steel-bottom)"/>
      </linearGradient>
      <radialGradient id="plate-sheen" cx="0.78" cy="0" r="0.55">
        <stop offset="0" stop-color="#8a8a8a" stop-opacity="0.35"/>
        <stop offset="1" stop-color="#8a8a8a" stop-opacity="0"/>
      </radialGradient>
      <radialGradient id="plate-vignette" cx="0.5" cy="0.35" r="0.8">
        <stop offset="0.5" stop-color="#000" stop-opacity="0"/>
        <stop offset="1" stop-color="#000" stop-opacity="0.55"/>
      </radialGradient>

      <!-- cloudy grime -->
      <filter id="grime" x="0" y="0" width="100%" height="100%">
        <feTurbulence type="fractalNoise" baseFrequency="0.008 0.012" numOctaves="5" seed="7"/>
        <feColorMatrix type="matrix" values="0 0 0 0 0.75  0 0 0 0 0.75  0 0 0 0 0.75  1.6 0 0 0 -0.75"/>
      </filter>
      <!-- fine grain -->
      <filter id="grain" x="0" y="0" width="100%" height="100%">
        <feTurbulence type="fractalNoise" baseFrequency="0.85" numOctaves="2" seed="3"/>
        <feColorMatrix type="matrix" values="0 0 0 0 0.8  0 0 0 0 0.8  0 0 0 0 0.8  1.4 0 0 0 -0.7"/>
      </filter>
      <!-- brushed scratches -->
      <filter id="brush" x="0" y="0" width="100%" height="100%">
        <feTurbulence type="fractalNoise" baseFrequency="0.9 0.006" numOctaves="3" seed="11"/>
        <feColorMatrix type="matrix" values="0 0 0 0 0.85  0 0 0 0 0.85  0 0 0 0 0.85  2.4 0 0 0 -1.35"/>
      </filter>
      <filter id="brush-dark" x="0" y="0" width="100%" height="100%">
        <feTurbulence type="fractalNoise" baseFrequency="0.7 0.008" numOctaves="2" seed="21"/>
        <feColorMatrix type="matrix" values="0 0 0 0 0  0 0 0 0 0  0 0 0 0 0  2.2 0 0 0 -1.2"/>
      </filter>

      <linearGradient id="lock-ring" x1="0.2" y1="0" x2="0.8" y2="1">
        <stop offset="0" stop-color="var(--ring-light)"/>
        <stop offset="0.4" stop-color="var(--ring-mid)"/>
        <stop offset="1" stop-color="var(--ring-dark)"/>
      </linearGradient>
      <linearGradient id="lock-face" x1="0" y1="0" x2="0" y2="1">
        <stop offset="0" stop-color="var(--face)"/>
        <stop offset="1" stop-color="var(--face-dark)"/>
      </linearGradient>
      <linearGradient id="screen-bezel" x1="0" y1="0" x2="0" y2="1">
        <stop offset="0" stop-color="#2a2a2a"/>
        <stop offset="1" stop-color="#474747"/>
      </linearGradient>
      <radialGradient id="status-led" cx="0.4" cy="0.35" r="0.7">
        <stop offset="0" stop-color="var(--led-glow)"/>
        <stop offset="1" stop-color="var(--led)"/>
      </radialGradient>
      <clipPath id="canvas-clip"><rect width="1200" height="646"/></clipPath>
      <clipPath id="face-clip"><circle cx="594" cy="318" r="106"/></clipPath>
      <clipPath id="ring-clip"><circle cx="594" cy="316" r="140"/></clipPath>
    </defs>

    <!-- steel door panels -->
    <g class="door-panels" role="img" aria-label="Brushed, scratched dark steel door surface" clip-path="url(#canvas-clip)">
      <rect width="1200" height="646" fill="url(#steel-plate)"/>
      <rect width="1200" height="646" fill="url(#plate-sheen)"/>
      <rect width="1200" height="646" filter="url(#grime)" opacity="0.22"/>
      <rect width="1200" height="646" filter="url(#grain)" opacity="0.12"/>
      <g transform="rotate(-32 600 323)">
        <rect x="-400" y="-500" width="2000" height="1650" filter="url(#brush)" opacity="0.28"/>
        <rect x="-400" y="-500" width="2000" height="1650" filter="url(#brush-dark)" opacity="0.35"/>
      </g>
      <rect width="1200" height="646" fill="url(#plate-vignette)"/>
    </g>

    <!-- centre seam wrapping around the lock -->
    <g class="door-seam" fill="none">
      <path d="M607 0 V158 Q607 170 593 171 A146 146 0 0 0 593 463 Q607 464 607 476 V646"
            stroke="var(--seam-dark)" stroke-width="6"/>
      <path d="M604 0 V158 Q604 168 592 169 A148 148 0 0 0 592 465 Q604 466 604 476 V646"
            stroke="var(--seam-light)" stroke-width="2"/>
    </g>

    <!-- lock housing -->
    <g class="lock">
      <circle cx="598" cy="322" r="140" fill="#050505" opacity="0.75"/>
      <circle cx="594" cy="316" r="140" fill="url(#lock-ring)"/>
      <g clip-path="url(#ring-clip)">
        <g transform="rotate(-32 594 316)">
          <rect x="420" y="140" width="360" height="360" filter="url(#brush)" opacity="0.3"/>
        </g>
      </g>
      <circle cx="596" cy="320" r="110" fill="#0c0c0c"/>
      <circle cx="594" cy="318" r="106" fill="url(#lock-face)"/>
      <g clip-path="url(#face-clip)">
        <rect x="480" y="205" width="230" height="230" filter="url(#grime)" opacity="0.2"/>
        <g transform="rotate(-32 594 318)">
          <rect x="450" y="170" width="300" height="300" filter="url(#brush)" opacity="0.22"/>
        </g>
      </g>

      <!-- display -->
      <rect class="lock-display-frame" x="511" y="272" width="176" height="88" fill="url(#screen-bezel)" stroke="var(--screen-frame)" stroke-width="2"/>
      <path class="lock-display-bevel" d="M519 279 H679 V353 H519 Z" fill="#4e4e4e"/>
      <path d="M519 279 H679 L673 284 H525 Z" fill="#222"/>
      <rect class="lock-display" x="525" y="284" width="148" height="63" fill="var(--screen)"/>

      <!-- status light -->
      <circle class="lock-led-rim" cx="596" cy="395" r="12" fill="#5c5c5c"/>
      <circle cx="596" cy="395" r="10" fill="#1a1a1a"/>
      <circle class="lock-led" cx="596" cy="395" r="8.5" fill="url(#status-led)"/>
    </g>
  </svg>
</main>
</body>
</html>
```